Word Template for KOREL Polls

KOREL Polls stands for 'Kindred Outlook Readings Entered Locally Polls'. It is a collaborative research effort to format and combine multiple sources of public opinion data from around the world into merged datasets. We need a Microsoft Word template design for our research reports, dataset codebooks, crowdsourced development guidelines, and other documents that will be produced as part of the research and development. The template should match the website design and logo, which are attached to this contest (these are the files from previous successful design contests).

The main purpose will be to write reports discussing research and analysis. There will be lots data visualizations (bar charts, scatter plots, pie charts, histograms, trend line charts etc.) as well as tables, diargams, and photos mixed in wit all the text. A second purpose will be to write guidebooks to describe processes and teach others how to manage data, find variables, and write code, which will include screenshots and Word are diagrams and figures.

There are some document uploaded as examples for the kinds of things for which we need the template (working papers, codebooks, pamphlets, etc)

Target Market(s)

academia, government, non-profits, postgraduates, researchers

Font styles to use
Serif

Colors

Designer to choose colors to be used in the design.

Requirements
Must have
• A4 size page template
• Cover page
• Must match website design and logo (see attached)
Nice to have
• Colors to match logo and website (see attached)

```html
<!DOCTYPE html>
<html lang="en">
<head>
<meta charset="utf-8">
<title>KOREL Polls – Codebook Cover</title>
<link href="https://fonts.googleapis.com/css2?family=Barlow:wght@500;600&family=Lato:wght@400&family=Nunito+Sans:wght@300;700&display=swap" rel="stylesheet">
<style>
  :root {
    --brand-blue: #1a5aa6;
    --brand-deep: #124f99;
    --band-light: #2a8fd0;
    --accent-orange: #ec6a3a;
    --ink: #111111;
    --slate: #5a5a5a;
    --body-grey: #555555;
    --paper: #ffffff;
  }
  * { margin: 0; padding: 0; box-sizing: border-box; }
  html, body { width: 859px; height: 1200px; overflow: hidden; background: var(--paper); }
  .page { position: relative; width: 859px; height: 1200px; background: var(--paper); font-family: "Lato", sans-serif; }

  .top-band {
    position: absolute; top: 0; left: 0; width: 100%; height: 42px;
    background: linear-gradient(90deg, var(--brand-deep) 0%, var(--band-light) 50%, var(--brand-deep) 100%);
    box-shadow: 0 3px 6px rgba(0,0,0,0.15);
  }
  .bottom-band {
    position: absolute; bottom: 0; left: 0; width: 100%; height: 38px;
    background: linear-gradient(90deg, var(--brand-deep) 0%, var(--band-light) 75%, #ffffff 100%);
  }

  .brand { position: absolute; top: 76px; left: 28px; display: flex; align-items: center; gap: 18px; }
  .brand-mark { width: 50px; height: 50px; border-radius: 50%; background: var(--brand-blue); }
  .brand-name { font-family: "Barlow", sans-serif; font-weight: 600; font-size: 40px; color: var(--brand-blue); letter-spacing: 0.5px; }

  .headline { position: absolute; top: 324px; left: 0; width: 100%; text-align: center; font-family: "Barlow", sans-serif; font-weight: 600; line-height: 1; }
  .headline-primary { font-size: 38px; color: var(--ink); }
  .headline-primary .accent { color: var(--accent-orange); }
  .headline-secondary { margin-top: 12px; font-size: 37px; color: var(--slate); letter-spacing: -0.5px; }

  .intro { position: absolute; top: 444px; left: 79px; width: 705px; font-size: 9.6px; line-height: 11.3px; color: var(--body-grey); }

  .desk-photo {
    position: absolute; top: 552px; left: 0; width: 859px; height: 214px;
    background: linear-gradient(90deg, #e7e5e3 0%, #f2f1f0 40%, #e4e4e4 70%, #9aa29c 90%, #1e2725 100%);
  }

  .doc-title { position: absolute; top: 882px; left: 14px; color: var(--brand-blue); font-family: "Nunito Sans", sans-serif; }
  .doc-title-main { font-size: 48px; font-weight: 700; line-height: 1; letter-spacing: -0.5px; }
  .doc-title-sub { font-size: 29px; font-weight: 700; line-height: 1; margin-top: 10px; }
  .doc-title-tag { font-size: 29px; font-weight: 300; line-height: 1; margin-top: 10px; }

  .section-heading { position: absolute; top: 1020px; left: 14px; font-family: "Barlow", sans-serif; font-weight: 600; font-size: 19px; color: var(--brand-blue); letter-spacing: -0.2px; }
  .section-lead { position: absolute; top: 1050px; left: 14px; width: 440px; font-size: 9.2px; line-height: 10.5px; color: var(--brand-blue); }
  .section-body { position: absolute; top: 1083px; left: 14px; width: 432px; font-size: 9.2px; line-height: 10.2px; color: var(--brand-blue); }
</style>
</head>
<body>
<div class="page">
  <div class="top-band"></div>

  <header class="brand">
    <span class="brand-mark"></span>
    <span class="brand-name">KOREL Polls</span>
  </header>

  <section class="headline">
    <div class="headline-primary"><span class="accent">KINDRED</span> OUTLOOK READINGS</div>
    <div class="headline-secondary">ENTERED LOCALLY POLLS</div>
  </section>

  <p class="intro">Sed ut perspiciatis unde omnis iste natus error sit voluptatem accusantium doloremque laudantium,explicabo. Nemo enim ipsam voluptatem quia consequuntur magni dolores eos qui ratione voluptatem sequi nesciunt. Neque porro quisquam est, qui dolorem ipsum quia dolor sit amet, consectetur, tempora incidunt ut labore et dolore magnam aliquam quaerat voluptatem. Ut enim ad minima veniam, quis nostrum exercitationem ullam</p>

  <div class="desk-photo" role="img" aria-label="Photo of a white desk with a laptop showing an infographic, art supplies, books, headphones and a potted succulent"></div>

  <section class="doc-title">
    <div class="doc-title-main">Codebook</div>
    <div class="doc-title-sub">for Country-Survey Data</div>
    <div class="doc-title-tag">LAYOUT</div>
  </section>

  <h2 class="section-heading">SED UT PERSPICIATIS UNDE SIT AMET</h2>
  <p class="section-lead">Curabitur at libero est, nec laoreet sapien. Duis rutrum,nuet tristique pharetra,<br>Curabitur at libero est, nec laoreet sapien. Duis rutrum,nuet tristique pharetra, neque</p>
  <p class="section-body">Sed ut perspiciatis unde omnis iste natus error sit voluptatem accusantium doloremque laudantium, totam rem aperiam, eaque ipsa quae ab illo inventore veritatis et quasi architecto beatae vitae dicta sunt explicabo. Nemo enim ipsam voluptatem quia voluptas sit aspernatur aut odit aut fugit, sed quia consequuntur magni dolores eos qui ratione voluptatem sequi nesciunt. Neque porro quisquam est, qui dolorem ipsum quia dolor sit amet, consectetur, adipisci velit, sed quia non numquam eius modi tempora incidunt ut labore et dolore magnam aliquam quaerat voluptatem. Ut enim ad minima veniam, quis nostrum exercitationem ullam corporis suscipit laboriosam, nisi ut aliquid ex</p>

  <div class="bottom-band"></div>
</div>
</body>
</html>
```